Redesign wellness clinic website

The project is redesign a wellness clinic http://www.thornleighvitality.example. The new website is to be responsive,clean,bright and a strong call to action which is to book an appointment. The logo will remain the same but the colour scheme on the website should be reflect purple white and green. I want it to be bright and cheerful and the feeling of clarity. The website shouldn't be overloaded with content but more visuals.

Target Market(s)

Anyone that has corporate wellness benefits within the downtown Toronto core. Majority of audience are professional working in Media, Telecommunications and Investments.

Industry/Entity Type

Health And Wellness

Number of Pages Required

5+ page

Font styles to use
Sans Serif

Colors
ffffff
886aae
acd036

Requirements
Must have
• -Strong call to action which is book an appointment like this page https://www.kestrelmotion.example/
• -Services provided icons on the page like https://www.brightpathvitalityhouse.example/
• - Pictures of a good visualizing a fit and healthy life
• - Strong ratings from Quorva, Zintrel, PostMaz, similar to this website http://www.summitbalancehealth.example/our-team-professionals/
• - Bright and clear
Should not have
• -No black and white images (redo our pictures)
• -Dark themes

```html
<!DOCTYPE html>
<html lang="en">
<head>
<meta charset="utf-8">
<title>Thornleigh Vitality Centre</title>
<link rel="stylesheet" href="https://fonts.googleapis.com/css2?family=Open+Sans:wght@400;600;700;800&display=swap">
<style>
:root{
  --purple:#886aae;
  --purple-dark:#6e5196;
  --green:#acd036;
  --green-dark:#8fb21f;
  --green-pale:#e4f0c2;
  --white:#ffffff;
  --ink:#3a3a3a;
  --muted:#6b6b6b;
  --line:#e2e2e2;
  --footer:#f3f3f3;
}
*{box-sizing:border-box;margin:0;padding:0}
html,body{width:1200px;height:2264px;overflow:hidden}
body{font-family:"Open Sans",Arial,sans-serif;color:var(--ink);background:var(--white);font-size:15px;line-height:1.55}
.wrap{width:1060px;margin:0 auto;position:relative}

/* header */
.site-header{height:64px;background:var(--white);border-bottom:1px solid var(--line)}
.site-header .wrap{height:64px;display:flex;align-items:center;justify-content:space-between}
.brand{display:flex;align-items:center;gap:10px}
.brand-mark{width:22px;height:22px;background:var(--green)}
.brand-name{font-weight:700;font-size:16px;color:var(--purple)}
.header-right{display:flex;flex-direction:column;align-items:flex-end;gap:4px}
.top-actions{display:flex;gap:26px;font-size:14px;font-weight:600;color:var(--purple)}
.top-actions span{display:flex;align-items:center;gap:6px}
.main-nav{display:flex;gap:30px;font-size:13px;font-weight:600;color:var(--ink)}
.main-nav .active{color:var(--green-dark)}

/* hero */
.hero{height:580px;position:relative;background:linear-gradient(110deg,#cfd4da 0%,#e9ebee 40%,#d8c9c2 70%,#b79b8e 100%)}
.hero-panel{position:absolute;left:170px;top:120px;width:470px;padding:26px 30px 30px;background:rgba(40,40,40,.78);color:var(--white)}
.hero-panel h1{font-size:34px;font-weight:700;line-height:1.2}
.hero-panel p{font-size:20px;line-height:1.35;margin-top:10px}
.btn{display:inline-block;background:var(--green);color:var(--white);font-weight:700;font-size:14px;padding:11px 26px;border-radius:2px;letter-spacing:.3px}
.hero-panel .btn{margin-top:22px;font-size:15px;padding:13px 28px}
.hero-arrow{position:absolute;top:270px;width:34px;height:34px}
.hero-arrow.prev{left:40px}.hero-arrow.next{right:40px}
.hero-dots{position:absolute;bottom:22px;left:50%;transform:translateX(-50%);display:flex;gap:8px}
.hero-dots i{width:10px;height:10px;border-radius:50%;background:rgba(255,255,255,.7)}
.hero-dots i.on{background:var(--green)}

/* about */
.about{height:280px;padding-top:30px}
.about .wrap{display:flex;gap:50px}
.about-text{width:560px}
h2.section-title{font-size:28px;font-weight:700;color:var(--ink);margin-bottom:14px}
.about-text p{font-size:13px;color:var(--muted);line-height:1.6}
.about-text .btn{margin-top:18px}
.review{flex:1}
.video{height:170px;background:linear-gradient(135deg,#8d8d8d,#5a5a5a);position:relative;display:flex;align-items:center;justify-content:center}

/* services */
.services{height:380px;background:var(--purple);padding-top:36px;text-align:center;color:var(--white)}
.services h2{font-size:30px;font-weight:700;margin-bottom:30px}
.service-list{display:flex;justify-content:space-between}
.service{width:160px}
.service-icon{width:84px;height:84px;border-radius:50%;background:var(--white);margin:0 auto 14px;display:flex;align-items:center;justify-content:center}
.service h3{font-size:16px;font-weight:700;color:var(--green);line-height:1.25;margin-bottom:6px}
.service p{font-size:12px;line-height:1.5}

/* callouts */
.callouts{height:270px;padding-top:34px}
.callouts .wrap{display:flex;gap:24px}
.mission{width:700px;height:210px;background:var(--green-pale);padding:24px 34px;text-align:center;color:var(--purple-dark)}
.mission .lead{font-size:21px;font-weight:700;line-height:1.35}
.mission p{font-size:14px;margin-top:12px}
.mission .contact{font-weight:700;margin-top:6px}
.location{flex:1;height:210px;background:var(--purple);color:var(--white);text-align:center;padding:22px 26px}
.location h3{font-size:20px;font-weight:700;margin-bottom:10px}
.location p{font-size:13px;line-height:1.5}
.location .btn{background:var(--purple-dark);margin-top:14px;padding:9px 22px}

/* ratings */
.ratings{height:250px;display:flex;justify-content:center;align-items:center;gap:40px}
.badge{width:150px;height:150px;border:1px solid var(--line);background:var(--white);box-shadow:0 2px 6px rgba(0,0,0,.08);display:flex;align-items:center;justify-content:center}
.badge .shape{width:90px;height:60px;border-radius:6px;background:#e8e8e8}
.badge.red .shape{background:#d32323}
.badge.solid{background:#e0322f;border-color:#e0322f}
.badge.solid .shape{background:#ffffff;opacity:.9}

/* footer */
.site-footer{height:340px;background:var(--footer);padding-top:34px}
.site-footer .wrap{display:flex;gap:40px}
.foot-col{width:160px}
.foot-col.wide{width:200px}
.foot-col h4{font-size:13px;font-weight:800;text-transform:uppercase;margin-bottom:10px;min-height:20px}
.foot-col li{list-style:none;font-size:13px;color:var(--muted);margin-bottom:6px}
.partners{margin-left:auto;width:200px}
.partner{display:flex;align-items:center;gap:10px;margin-top:8px}
.partner .dot{width:26px;height:26px;border-radius:50%;background:var(--purple)}
.partner span{font-weight:700;font-size:15px;color:var(--purple-dark)}

.bottom-bar{height:104px;display:flex;align-items:center}
.bottom-bar .wrap{display:flex;align-items:center;gap:14px}
.bottom-bar .mark{width:26px;height:26px;background:var(--green)}
.bottom-bar p{font-size:12px;color:var(--muted);line-height:1.4}
</style>
</head>
<body>

<header class="site-header">
  <div class="wrap">
    <div class="brand"><span class="brand-mark"></span><span class="brand-name">Thornleigh Vitality Centre</span></div>
    <div class="header-right">
      <div class="top-actions">
        <span><svg width="16" height="16" viewBox="0 0 16 16"><rect x="1.5" y="3" width="13" height="11" rx="1.5" fill="none" stroke="#886aae" stroke-width="1.6"/><line x1="1.5" y1="6.5" x2="14.5" y2="6.5" stroke="#886aae" stroke-width="1.6"/><line x1="5" y1="1" x2="5" y2="4" stroke="#886aae" stroke-width="1.6"/><line x1="11" y1="1" x2="11" y2="4" stroke="#886aae" stroke-width="1.6"/></svg>Book An Appointment</span>
        <span><svg width="16" height="16" viewBox="0 0 16 16"><path d="M4 1.5l2.2 3-1.4 1.6c.8 1.9 2.3 3.4 4.1 4.2l1.6-1.4 3 2.2-1.3 2.6C7 13.4 2.6 9 2.3 3z" fill="#886aae"/></svg>416-555-0182</span>
      </div>
      <nav class="main-nav">
        <span class="active">Home</span><span>Fees and Services</span><span>Our Staff</span><span>News and Updates</span><span>Corporate Wellness</span><span>Forms</span><span>Contact</span>
      </nav>
    </div>
  </div>
</header>

<section class="hero" role="img" aria-label="Photo of a practitioner treating a client's leg in a bright clinic room">
  <svg class="hero-arrow prev" viewBox="0 0 34 34"><path d="M21 7L11 17l10 10" fill="none" stroke="#fff" stroke-width="3"/></svg>
  <div class="hero-panel">
    <h1>Thornleigh Vitality Centre</h1>
    <p>Chiropractic and Wellness Center Based in Downtown Toronto.</p>
    <span class="btn">BOOK AN APPOINTMENT</span>
  </div>
  <svg class="hero-arrow next" viewBox="0 0 34 34"><path d="M13 7l10 10-10 10" fill="none" stroke="#fff" stroke-width="3"/></svg>
  <div class="hero-dots"><i class="on"></i><i></i><i></i></div>
</section>

<section class="about">
  <div class="wrap">
    <div class="about-text">
      <h2 class="section-title">About Thornleigh Vitality Centre</h2>
      <p>Established in 1989 the Thornleigh Vitality Centre has become one of Canada's leaders in providing quality care and innovative programs for the community. The founder and director Dr. Elena Marsh's vision has come to life with over 30 practitioners providing a multitude of different services under one roof. Some of the services include Chiropractic, Physiotherapy, Athletic Therapy, Naturopathic Therapy, Acupuncture and Personal Training.</p>
      <span class="btn">Read More</span>
    </div>
    <div class="review">
      <h2 class="section-title">Review Video</h2>
      <div class="video" role="img" aria-label="Video still of a client review in the clinic">
        <svg width="60" height="60" viewBox="0 0 60 60"><circle cx="30" cy="30" r="28" fill="rgba(0,0,0,.45)"/><path d="M24 18l18 12-18 12z" fill="#fff"/></svg>
      </div>
    </div>
  </div>
</section>

<section class="services">
  <h2>Our Services</h2>
  <div class="wrap service-list">
    <div class="service">
      <div class="service-icon"><svg width="44" height="44" viewBox="0 0 44 44"><rect x="19" y="4" width="6" height="36" rx="3" fill="#886aae"/><rect x="12" y="10" width="20" height="4" rx="2" fill="#886aae"/><rect x="12" y="19" width="20" height="4" rx="2" fill="#886aae"/><rect x="12" y="28" width="20" height="4" rx="2" fill="#886aae"/></svg></div>
      <h3>Chiropractic</h3>
      <p>Chiropractic is a non invasive, hands on health care.</p>
    </div>
    <div class="service">
      <div class="service-icon"><svg width="44" height="44" viewBox="0 0 44 44"><circle cx="22" cy="9" r="5" fill="#886aae"/><path d="M12 20h20l-4 6v14h-4V30h-4v10h-4V26z" fill="#886aae"/></svg></div>
      <h3>Physiotherapy</h3>
      <p>Physiotherapy is a drug free health care practice.</p>
    </div>
    <div class="service">
      <div class="service-icon"><svg width="44" height="44" viewBox="0 0 44 44"><rect x="4" y="16" width="6" height="12" rx="1" fill="#886aae"/><rect x="34" y="16" width="6" height="12" rx="1" fill="#886aae"/><rect x="10" y="20" width="24" height="4" fill="#886aae"/></svg></div>
      <h3>Active Rehabilitation</h3>
      <p>The personal training aspect at our Centre is one that most value.</p>
    </div>
    <div class="service">
      <div class="service-icon"><svg width="44" height="44" viewBox="0 0 44 44"><path d="M6 28c8-6 24-6 32 0v4H6z" fill="#886aae"/><circle cx="14" cy="20" r="4" fill="#886aae"/></svg></div>
      <h3>Massage Therapy</h3>
      <p>Massage Therapy is done on a table with the client robed.</p>
    </div>
    <div class="service">
      <div class="service-icon"><svg width="44" height="44" viewBox="0 0 44 44"><path d="M22 38s-14-9-14-19a8 8 0 0 1 14-5 8 8 0 0 1 14 5c0 10-14 19-14 19z" fill="#886aae"/></svg></div>
      <h3>Osteopathy</h3>
      <p>Osteopathy is patient centred treatment that enhances the body.</p>
    </div>
    <div class="service">
      <div class="service-icon"><svg width="44" height="44" viewBox="0 0 44 44"><path d="M10 34C10 18 22 8 36 8c0 16-10 26-26 26z" fill="#886aae"/><path d="M10 34L26 18" stroke="#fff" stroke-width="2"/></svg></div>
      <h3>Nutrition &amp; Lifestyle Medicine</h3>
      <p>Naturopathic medicine is a distinct primary health care system.</p>
    </div>
  </div>
</section>

<section class="callouts">
  <div class="wrap">
    <div class="mission">
      <p class="lead">Our Centre is committed to helping improve and extend the lives of as many people as possible in our communities.</p>
      <p>Come and join our family and start changing your life today.<br>Planning a wellness talk? We can help!</p>
      <p class="contact">Contact us at info@thornleighvitality.example for more details.</p>
    </div>
    <div class="location">
      <h3>Visit Our New Location</h3>
      <p>We are open for business at 7:30 am,<br>7 days a week!</p>
      <p style="margin-top:8px">Visit one of our associates about our Referral Reward Program.</p>
      <span class="btn">See Map</span>
    </div>
  </div>
</section>

<section class="ratings" aria-label="Ratings from Zintrel, Quorva and PostMaz">
  <div class="badge" aria-label="Zintrel rating"><span class="shape"></span></div>
  <div class="badge red" aria-label="Quorva rating"><span class="shape"></span></div>
  <div class="badge solid" aria-label="PostMaz rating"><span class="shape"></span></div>
</section>

<footer class="site-footer">
  <div class="wrap">
    <div class="foot-col">
      <h4>Site Map</h4>
      <ul><li>Home</li><li>Fees and Services</li><li>Our Staff</li><li>News and Updates</li></ul>
    </div>
    <div class="foot-col">
      <h4>&nbsp;</h4>
      <ul><li>Corporate Wellness</li><li>Forms</li><li>Contact</li></ul>
    </div>
    <div class="foot-col">
      <h4>Services</h4>
      <ul><li>Chiropractic</li><li>Physiotherapy</li><li>Active Rehabilitation</li><li>Massage Therapy</li></ul>
    </div>
    <div class="foot-col wide">
      <h4>&nbsp;</h4>
      <ul><li>Nutrition and Lifestyle Medicine</li><li>Osteopathy</li><li>Orthotics</li></ul>
    </div>
    <div class="partners">
      <h4 style="font-size:13px;font-weight:800;text-transform:uppercase">Our Partners</h4>
      <div class="partner"><span class="dot"></span><span>Harlow Dental Centre</span></div>
    </div>
  </div>
</footer>

<div class="bottom-bar">
  <div class="wrap">
    <span class="mark"></span>
    <p>Copyright © 2016, Company Name.<br>All Rights Reserved.</p>
  </div>
</div>

</body>
</html>
```